We need a design for our retail display and for our stockist's retail display.
Our product is fresh corn tortillas. These can be used to make tacos, quesadillas, tortilla chips and tostadas.
We want the table talker to use our brand style (see our website) and show the tortillas versatility.
verdel-foods.co.uk
It should also have a space for our stockists to write in a blank space under the heading "Our fresh tortillas are delivered every....[blank space]"
The table talker should be 75mm tall x 150mm wide. This will also have a 25mm self adhesive flap at the top which can be blank or the same colour as the background.
Please feel free to use any files from our website as well as illustrations attached.
Customers in high end shops and delis
food and drink

```html
<!DOCTYPE html>
<html lang="en">
<head>
<meta charset="utf-8">
<title>Verdel Tortillas – Table Talker</title>
<link rel="stylesheet" href="https://fonts.googleapis.com/css2?family=Fredoka:wght@500;600;700&display=swap">
<style>
  :root {
    --navy: #1c2a45;
    --navy-soft: #24355a;
    --navy-line: #2b3a58;
    --yellow: #e8c125;
    --white: #ffffff;
    --page: #e9e9e9;
    --tortilla-light: #f3ead8;
    --tortilla-mid: #d9c39a;
    --tortilla-dark: #b89a66;
  }
  * { margin: 0; padding: 0; box-sizing: border-box; }
  html, body {
    width: 1200px;
    height: 672px;
    overflow: hidden;
    background: var(--page);
  }
  .canvas {
    position: relative;
    width: 1200px;
    height: 672px;
  }
  .table-talker {
    position: absolute;
    left: 40px;
    top: 55px;
    width: 910px;
    height: 456px;
    transform: scale(1.2308);
    transform-origin: 0 0;
    overflow: hidden;
    background: var(--navy);
    font-family: "Fredoka", sans-serif;
  }
  .pattern-field {
    position: absolute;
    inset: 0 0 148px 0;
    background:
      radial-gradient(ellipse 60% 40% at 30% 30%, var(--navy-soft) 0%, transparent 70%),
      radial-gradient(ellipse 50% 45% at 80% 65%, var(--navy-soft) 0%, transparent 70%),
      var(--navy);
  }
  .flap-fold {
    position: absolute;
    left: 0; right: 0;
    top: 150px;
    height: 1px;
    background: var(--navy-line);
  }
  .band-write-in {
    position: absolute;
    left: 0; right: 0;
    top: 306px;
    height: 77px;
    background: var(--white);
  }
  .band-base {
    position: absolute;
    left: 0; right: 0;
    top: 383px;
    height: 73px;
    background: var(--yellow);
  }
  .photo-frame {
    position: absolute;
    left: 48px;
    top: 168px;
    width: 254px;
    height: 254px;
    border-radius: 50%;
    background: var(--navy);
    border: 2px solid var(--yellow);
    padding: 7px;
  }
  .photo-frame .photo {
    width: 100%;
    height: 100%;
    border-radius: 50%;
    background: radial-gradient(circle at 40% 58%, var(--tortilla-mid) 0%, var(--tortilla-dark) 40%, var(--tortilla-light) 64%, var(--white) 100%);
  }
  .brand-badge {
    position: absolute;
    left: 267px;
    top: 246px;
    width: 156px;
    height: 156px;
    border-radius: 50%;
    background: var(--navy);
    display: flex;
    align-items: center;
    justify-content: center;
  }
  .brand-name {
    color: var(--yellow);
    font-weight: 600;
    font-size: 40px;
    line-height: 1;
  }
  .headline {
    position: absolute;
    right: 50px;
    top: 155px;
    color: var(--yellow);
    font-weight: 600;
    line-height: 1;
    white-space: nowrap;
    text-align: right;
  }
  .headline-line {
    display: flex;
    justify-content: flex-end;
    align-items: baseline;
    gap: 12px;
    font-size: 54px;
  }
  .headline-line + .headline-line { margin-top: 12px; }
  .headline-accent {
    font-size: 80px;
    font-weight: 700;
    letter-spacing: -1px;
  }
  .write-in-prompt {
    position: absolute;
    left: 528px;
    top: 306px;
    color: var(--navy);
    font-weight: 700;
    font-size: 56px;
    line-height: 1;
  }
  .claims {
    position: absolute;
    left: 470px;
    top: 395px;
    display: flex;
    gap: 11px;
    list-style: none;
  }
  .claims li {
    width: 48px;
    height: 48px;
    border-radius: 50%;
    background: var(--navy);
    border: 2px solid var(--navy);
    box-shadow: inset 0 0 0 1.5px var(--yellow);
    color: var(--white);
    display: flex;
    flex-direction: column;
    align-items: center;
    justify-content: center;
    text-align: center;
    line-height: 1;
    font-weight: 600;
  }
  .claim-big { font-size: 11px; }
  .claim-small { font-size: 5.5px; letter-spacing: 0.1px; margin-top: 1px; }
  .claim-caps { font-size: 10px; text-transform: uppercase; }
</style>
</head>
<body>
<main class="canvas">
  <section class="table-talker" aria-label="Verdel Tortillas table talker">
    <div class="pattern-field" role="img" aria-label="Repeating outline taco pattern on navy"></div>
    <div class="flap-fold"></div>
    <div class="band-write-in"></div>
    <div class="band-base"></div>

    <div class="photo-frame">
      <div class="photo" role="img" aria-label="Tall stack of fresh corn tortillas"></div>
    </div>

    <div class="brand-badge">
      <span class="brand-name">verdel</span>
    </div>

    <h1 class="headline">
      <span class="headline-line"><span>Our</span><span class="headline-accent">fresh</span><span>Tortillas</span></span>
      <span class="headline-line"><span>are delivered</span></span>
    </h1>
    <p class="write-in-prompt">Every...</p>

    <ul class="claims" aria-label="Product claims">
      <li><span class="claim-big">vegan</span></li>
      <li><span class="claim-big">100%</span><span class="claim-small">RECYCLABLE</span></li>
      <li><span class="claim-caps">No</span><span class="claim-caps">GMO</span></li>
      <li><span class="claim-big">no</span><span class="claim-small">PRESERVATIVES</span></li>
      <li><span class="claim-big">gluten</span><span class="claim-small">FREE</span></li>
    </ul>
  </section>
</main>
</body>
</html>
```